Buchcover-Design für psychologischen Ratgeber Morgens voller Mut!
Zielgruppe
Veröffentlichung psychologischer Ratgeber. Zielgruppe sind Erwachsene.
Aufgabenstellung
keine besondere Vorgaben, ein eyecatching-Cover wäre super. Der Titel des Buches lautet: Morgens voller Mut! Der Untertitel lautet: Heitere Seelenkunde für stille Kraft und Zuversicht
Autoren: Dr. Hanna Wiesmoor-Kalbach, Dr. Lukas Kalbach
Vielleicht macht es Sinn, einen Button mit: 199 Praxistipps auf dem Cover anzuführen.
Das Buch wird als Softcover und Ebook auf lesewelt veröffentlicht. Das Format ist 6 mal 9 Zoll und hat 425 Seiten.

```html
<!DOCTYPE html>
<html lang="de">
<head>
<meta charset="utf-8">
<title>Morgens voller Mut! – Buchumschlag</title>
<link href="https://fonts.googleapis.com/css2?family=Rubik:wght@500;700;800&family=Raleway:wght@300;400&display=swap" rel="stylesheet">
<style>
  :root {
    --page: #ffffff;
    --blue-deep: #2a67c4;
    --blue-1: #3274d0;
    --blue-2: #4a88dc;
    --blue-3: #66a0e8;
    --blue-4: #86bbfa;
    --title-blue: #2a62c0;
    --sub-green: #4fa866;
    --ink: #222222;
    --t-purple: #9a82d8;
    --t-yellow: #f4bd48;
    --t-pink: #e994cb;
    --t-sky: #78ade9;
    --t-coral: #f0725f;
    --t-rose: #df7fc0;
    --t-blue: #5c9be6;
    --t-green: #58ae6e;
    --t-orange: #f1a23d;
    --t-lavender: #6a86d6;
    --t-violet: #a481d2;
  }
  html, body { margin: 0; padding: 0; width: 698px; height: 1200px; overflow: hidden; background: var(--page); }
  .canvas { position: relative; width: 698px; height: 1200px; }
  .cover-wrap {
    position: absolute; left: 19px; top: 369px;
    width: 1392px; height: 975px;
    transform: scale(0.4741); transform-origin: 0 0;
    background: var(--page); overflow: hidden;
  }
  .band { position: absolute; left: 0; width: 1392px; height: 173px; display: flex; flex-direction: column; }
  .band--top { top: 0; height: 175px; }
  .band--bottom { top: 802px; flex-direction: column-reverse; }
  .band span { flex: 1; }
  .band span:nth-child(1) { background: var(--blue-deep); flex: 0.8; }
  .band span:nth-child(2) { background: var(--blue-1); }
  .band span:nth-child(3) { background: var(--blue-2); }
  .band span:nth-child(4) { background: var(--blue-3); }
  .band span:nth-child(5) { background: var(--blue-4); }
  .tile { position: absolute; width: 149px; height: 150px; }
  .tile--purple { background-color: var(--t-purple); }
  .tile--yellow { background-color: var(--t-yellow); }
  .tile--pink { background-color: var(--t-pink); }
  .tile--sky { background-color: var(--t-sky); }
  .tile--coral { background-color: var(--t-coral); }
  .tile--rose { background-color: var(--t-rose); }
  .tile--blue { background-color: var(--t-blue); }
  .tile--green { background-color: var(--t-green); }
  .tile--orange { background-color: var(--t-orange); }
  .tile--lavender { background-color: var(--t-lavender); }
  .tile--violet { background-color: var(--t-violet); }
  .portrait::after {
    content: ""; position: absolute; inset: 0;
    background: linear-gradient(180deg, rgba(255,255,255,0) 55%, rgba(60,50,50,0.22) 100%);
  }
  .back-blurb {
    position: absolute; left: 205px; top: 225px; width: 395px;
    font-family: "Raleway", sans-serif; font-weight: 300; font-size: 17.4px; line-height: 27.8px;
    color: var(--ink); text-align: justify;
  }
  .back-blurb p { margin: 0 0 27.8px; }
  .spine {
    position: absolute; left: 672px; top: 192px; height: 620px;
    writing-mode: vertical-rl; display: flex; flex-direction: column; align-items: flex-start;
  }
  .spine-title { font-family: "Rubik", sans-serif; font-weight: 800; font-size: 40px; color: var(--title-blue); letter-spacing: 0.5px; margin: 0; line-height: 44px; white-space: nowrap; }
  .spine-authors { font-family: "Rubik", sans-serif; font-weight: 700; font-size: 12.5px; color: var(--ink); line-height: 16px; margin: 12px 0 0 4px; white-space: nowrap; }
  .front-title {
    position: absolute; left: 795px; top: 340px; margin: 0;
    font-family: "Rubik", sans-serif; font-weight: 800; font-size: 68px; line-height: 68px;
    color: var(--title-blue); letter-spacing: 0.5px;
  }
  .front-title span { display: block; }
  .front-title .line-2 { padding-left: 80px; }
  .front-authors {
    position: absolute; left: 1188px; top: 350px; margin: 0;
    font-family: "Rubik", sans-serif; font-weight: 700; font-size: 15px; line-height: 18px; color: var(--ink);
  }
  .front-subtitle {
    position: absolute; left: 882px; top: 498px; margin: 0;
    font-family: "Rubik", sans-serif; font-weight: 700; font-size: 27px; line-height: 31px;
    color: var(--sub-green); text-transform: uppercase;
  }
  .tips-badge { display: flex; flex-direction: column; justify-content: center; padding-left: 24px; box-sizing: border-box; color: #fff; font-family: "Rubik", sans-serif; }
  .tips-badge .count { font-weight: 700; font-size: 56px; line-height: 52px; }
  .tips-badge .label { font-weight: 500; font-size: 12.5px; letter-spacing: 0.3px; }
</style>
</head>
<body>
<main class="canvas">
  <section class="cover-wrap" aria-label="Buchumschlag mit Rückseite, Buchrücken und Vorderseite">
    <div class="band band--top"><span></span><span></span><span></span><span></span><span></span></div>
    <div class="band band--bottom"><span></span><span></span><span></span><span></span><span></span></div>

    <!-- Rückseite -->
    <div class="tile tile--purple portrait" style="left:23px;top:25px" role="img" aria-label="Porträtfoto eines lachenden jungen Mannes"></div>
    <div class="tile tile--yellow portrait" style="left:23px;top:175px;height:148px" role="img" aria-label="Porträtfoto einer lächelnden Frau mit roten Haaren"></div>
    <div class="tile tile--green" style="left:23px;top:323px;height:164px"></div>
    <div class="tile tile--coral portrait" style="left:23px;top:487px" role="img" aria-label="Porträtfoto einer lächelnden Frau mit dunklen Haaren"></div>
    <div class="tile tile--rose portrait" style="left:23px;top:637px;height:148px" role="img" aria-label="Porträtfoto einer zwinkernden Frau"></div>
    <div class="tile tile--lavender" style="left:23px;top:785px;height:163px"></div>

    <div class="back-blurb">
      <p>Was macht uns glücklich? Das ist seit jeher eine Kernfrage des Menschen. Nach wissenschaftlichen Erkenntnissen der Positiven Psychologie können wir durch bestimmte Verhaltensweisen 40 Prozent unseres Glücksniveaus selbst beeinflussen. Auch und gerade in schwierigen Alltagssituationen ist durch einfache psychologische Übungen eine Steigerung des Glücksempfindens und der Lebensfreude möglich.</p>
      <p>Welche Verhaltensweisen für ein von Glück erfülltes Leben besonders förderlich sind, beschreiben die Autoren Dr. Hanna Wiesmoor-Kalbach, promovierte Psychologin, Psychotherapeutin sowie Lehrtherapeutin für Verhaltenstherapie, und Coach Dr. Lukas Kalbach anschaulich anhand von 199 Praxistipps und Übungen. Zudem enthält das Buch 21 Tests und Fragebogen zur Selbstreflexion samt QR-Codes und Downloadlinks zum Ausdrucken.</p>
    </div>

    <!-- Buchrücken -->
    <div class="spine">
      <p class="spine-authors">Dr. Hanna Wiesmoor-Kalbach, Dr. Lukas Kalbach</p>
      <p class="spine-title">MORGENS VOLLER MUT!</p>
    </div>

    <!-- Vorderseite -->
    <div class="tile tile--sky portrait" style="left:769px;top:25px" role="img" aria-label="Porträtfoto einer lachenden Frau mit braunen Haaren"></div>
    <div class="tile tile--purple portrait" style="left:918px;top:25px" role="img" aria-label="Porträtfoto eines lachenden jungen Mannes"></div>
    <div class="tile tile--yellow" style="left:1067px;top:25px"></div>
    <div class="tile tile--pink portrait" style="left:1216px;top:25px" role="img" aria-label="Porträtfoto eines lachenden Mannes mit Bart"></div>
    <div class="tile tile--yellow portrait" style="left:769px;top:175px;height:148px" role="img" aria-label="Porträtfoto einer lächelnden Frau mit roten Haaren"></div>
    <div class="tile tile--coral portrait" style="left:918px;top:175px;height:148px" role="img" aria-label="Porträtfoto einer lächelnden Frau mit dunklen Haaren"></div>
    <div class="tile tile--rose portrait" style="left:1067px;top:175px;height:148px" role="img" aria-label="Porträtfoto einer zwinkernden Frau"></div>
    <div class="tile tile--blue portrait" style="left:1216px;top:175px;height:148px" role="img" aria-label="Porträtfoto eines staunend lachenden Mannes"></div>

    <h1 class="front-title"><span>MORGENS</span><span class="line-2">VOLLER MUT!</span></h1>
    <p class="front-authors">Dr. Hanna<br>Wiesmoor-Kalbach,<br>Dr. Lukas Kalbach</p>
    <p class="front-subtitle">Heitere<br>Seelenkunde für<br>stille Kraft<br>und Zuversicht</p>

    <div class="tile tile--green portrait" style="left:1216px;top:502px" role="img" aria-label="Porträtfoto eines lächelnden jungen Mannes"></div>
    <div class="tile tile--green" style="left:769px;top:652px"></div>
    <div class="tile tile--pink portrait" style="left:918px;top:652px" role="img" aria-label="Porträtfoto eines lachenden jungen Mannes"></div>
    <div class="tile tile--orange portrait" style="left:1067px;top:652px" role="img" aria-label="Porträtfoto einer lachenden Frau"></div>
    <div class="tile tile--blue portrait" style="left:1216px;top:652px" role="img" aria-label="Porträtfoto einer lächelnden Frau mit Haarknoten"></div>
    <div class="tile tile--lavender portrait" style="left:769px;top:802px;height:148px" role="img" aria-label="Porträtfoto eines lächelnden Mannes"></div>
    <div class="tile tile--violet tips-badge" style="left:918px;top:802px;height:148px">
      <span class="count">199</span>
      <span class="label">PRAXISTIPPS</span>
    </div>
    <div class="tile tile--green portrait" style="left:1067px;top:802px;height:148px" role="img" aria-label="Porträtfoto einer lächelnden Frau"></div>
    <div class="tile tile--violet portrait" style="left:1216px;top:802px;height:148px" role="img" aria-label="Porträtfoto eines lachenden Mannes mit Bart"></div>
  </section>
</main>
</body>
</html>
```